Quiet Ledger needs a book cover

Enabling people to find a new way of looking at money. If peoples thoughts, attitude and emotions around money are not inline with their goals and dreams then it is often harder to achieve their version of success.

Recognition that we have an emotional and a practical way with money.

Quiet Ledger enables people to find a sustainable (balanced) way with money for their life right now and their future.

Developing this over the years and seeing clients achieve a clear picture/idea/thought connection that is positive around money and it's purpose to them in their lives has truly been fabulous as they have then gone on to achieve their goals and dreams.

Title of book = Quiet Ledger
Tag line = Being healthy being wealthy
Authors Name = Ruth Pell
Book Size = 135 width x 185 height
Thumbnail = Cover must work well as well as full size
Looking for simple and clear app-able / icon type image
Feel free to have fun with it
A simple yet refreshing balanced, eye-catching design.

The back will include authors photo, blurb, testimonials, barcode, ISBN number & price. I will provide once front cover is sorted.

Reason: Realised that the tag line for the book was incorrect.

Target Market(s)

Individuals

Industry/Entity Type

Work

Requirements
Must have
• First work on front cover, once approved we can then do spine and back cover

```html
<!DOCTYPE html>
<html lang="en">
<head>
<meta charset="utf-8">
<title>Quiet Ledger – Book Cover</title>
<link href="https://fonts.googleapis.com/css2?family=Archivo+Black&family=Cinzel:wght@500;600&family=Open+Sans:wght@300&display=swap" rel="stylesheet">
<style>
  :root {
    --backdrop: #bcbdbf;
    --magenta: #e0097a;
    --white: #ffffff;
    --night: #0e171e;
    --deep-teal: #12303d;
    --glow-teal: #2a6478;
    --head-blue: #7cc8ec;
    --head-red: #e8232f;
  }
  * { margin: 0; padding: 0; box-sizing: border-box; }
  html, body {
    width: 1200px;
    height: 1192px;
    overflow: hidden;
    background: var(--backdrop);
  }
  .cover {
    position: absolute;
    left: 245px;
    top: 56px;
    width: 710px;
    height: 1069px;
    background: var(--night);
    overflow: hidden;
  }
  .title-band {
    position: absolute;
    left: 0; top: 0;
    width: 100%;
    height: 226px;
    background: var(--magenta);
  }
  .cover-backdrop {
    position: absolute;
    left: 0; top: 226px;
    width: 100%;
    height: 755px;
    background:
      radial-gradient(ellipse at 50% 45%, var(--glow-teal) 0%, var(--deep-teal) 45%, var(--night) 85%);
  }
  .cover-art {
    position: absolute;
    left: 0;
    top: 500px;
    width: 100%;
    height: 270px;
    background:
      radial-gradient(ellipse 95px 125px at 50% 50%, var(--head-red) 0%, rgba(232,35,47,0.85) 55%, rgba(232,35,47,0) 100%),
      radial-gradient(ellipse 85px 110px at 18% 55%, var(--head-blue) 0%, rgba(124,200,236,0.7) 55%, rgba(124,200,236,0) 100%),
      radial-gradient(ellipse 70px 110px at 97% 55%, var(--head-blue) 0%, rgba(124,200,236,0.7) 55%, rgba(124,200,236,0) 100%);
  }
  .title {
    position: absolute;
    left: 0; top: 0;
    width: 710px;
    height: 420px;
  }
  .title-light {
    font-family: "Open Sans", sans-serif;
    font-weight: 300;
    fill: var(--white);
  }
  .title-heavy {
    font-family: "Archivo Black", sans-serif;
    fill: var(--magenta);
  }
  .tagline {
    position: absolute;
    left: 0;
    top: 816px;
    width: 100%;
    text-align: center;
    font-family: "Cinzel", serif;
    font-weight: 600;
    font-size: 46px;
    line-height: 56px;
    color: var(--white);
    text-transform: uppercase;
  }
  .author-band {
    position: absolute;
    left: 0; bottom: 0;
    width: 100%;
    height: 88px;
    background: var(--magenta);
    display: flex;
    align-items: center;
    justify-content: center;
  }
  .author {
    font-family: "Cinzel", serif;
    font-weight: 600;
    font-size: 46px;
    letter-spacing: 0.22em;
    color: var(--white);
    text-transform: uppercase;
    padding-left: 0.22em;
  }
</style>
</head>
<body>
  <main class="cover">
    <div class="title-band"></div>
    <div class="cover-backdrop"></div>
    <div class="cover-art" role="img" aria-label="Three head silhouettes in profile on a dark digital code background, the centre head red and filled with currency symbols, the outer two pale blue"></div>

    <svg class="title" viewBox="0 0 710 420" aria-label="Quiet Ledger">
      <text class="title-light" x="72" y="198" font-size="180" textLength="605" lengthAdjust="spacingAndGlyphs">QUIET</text>
      <text class="title-heavy" x="70" y="387" font-size="186" textLength="610" lengthAdjust="spacingAndGlyphs">LEDGER</text>
    </svg>

    <p class="tagline">Being healthy<br>being wealthy</p>

    <footer class="author-band">
      <span class="author">Ruth Pell</span>
    </footer>
  </main>
</body>
</html>
```